Professional Hairdresser needs powerful, clever, simple, modern business card

I need a professional, clever, powerful, bold, attractive, modern/simplistic business card.
I specialize in dimensional hair color, precision haircutting, modern classic design, and signature finishes.
I believe in advanced education, continued training with emphasis on perfect practice, and strive to be the best at what I do.
I am trained by the industry's best and have passion for what I do, I want my business card to reflect my talents, education, capabilities, signature color techniques and design and confidence.
I want to be known as reputable, bold, artistic, aware, classic yet modern, innovative, creative, dimensional, knowledgeable, and educated.
I want something bold, simple, elegant, modern, clever, and legible.
My personal style is progressive, modern, eclectic, clean with modern luxury comfort style.
I love the use of black and white, to creative visual interest and texture. I think putting black as a solid background with white bold font makes the words jump/glow to the eye. I also think a stark white background with bold black fonts looks great, maybe with a punch of red. It is simple, clean, elegant.
I have a QR code I would like to include on the card but have no idea how to make it visually pleasing or make sense.
I do not have a set logo and am not sure if this needs to be done first or if the business card should be done first.

Target Market(s)

Early 20's-mid 60's, female and male, fashion aware, people who can afford my prices, appreciate value

Industry/Entity Type

Training

Requirements
Must have
• I would like to incorporate the QR code I have if possible.
I would like to have my name and contact info.
I would like my logo (or maybe have my logo be RT in a font like listed below).
I would like the fonts to be modern, bold, clean, readable.
Fonts I have looked at are: The font used on the book called: Vexaro A Hundred Years of Hue" I really love. I have looked at glyphvault.example for font and found "Georgiquas", but the designer wanted 200 euros which I just dont have at the time. Others I looked at include "Lin Libertine", Alien-Encounters-solid-regular-italic".
I love font used in the picture I included with the Tobin.Ashcroft ad.
Clean, modern, professional, legible, structured.
Nice to have
• I envision a black background with bold, modern, simple, font in white creating the effect of the words jumping off the card, visually apparent and glowing. Like a really expensive restaurant with a sign that you cant miss because the name is in bright white on black background, simple, bold, modern but not futuristic, powerful, clever, elegant, and draws the eye making it unforgetable. Perhaps layering black and white in order to where the font will be in white.
I see balance and chic.
Perhaps
Should not have
• I appreciate the trends in business design, but realize trends come and go and not sure if having something "trendy" is advisable for me. Having said that, I like creative modern design and sometimes current trends are important in design. I do like red as accent color, the primary blue color, blue on the PixelForum page, the masculine/florescent purple, and the neo bold yellow and the primary color shade of yellow.
I do not want clutter.
I do not want any fonts that are swirly, old-world calligraphy, script, or penmanship style.
I do not want picture of scissors, heads of old-school beauty school hair, or barber poles.

```html
<!DOCTYPE html>
<html lang="en">
<head>
<meta charset="utf-8">
<title>Rowan Tate – Professional Hair Designer</title>
<link rel="stylesheet" href="https://fonts.googleapis.com/css2?family=Michroma&family=Arimo:wght@700&display=swap">
<style>
  :root {
    --accent-red: #c8161d;
    --card-black: #050505;
    --sheen-light: #4b4d4e;
    --sheen-dark: #161616;
    --name-silver: #e4e6e8;
    --tagline-white: #f4f4f4;
    --rule-glow: #ffffff;
  }
  html, body {
    margin: 0;
    padding: 0;
    width: 1200px;
    height: 600px;
    overflow: hidden;
    background: var(--accent-red);
  }
  .business-card {
    display: block;
    width: 1200px;
    height: 600px;
  }
  .card-face { fill: var(--card-black); }
  .sheen-top { stop-color: var(--sheen-light); }
  .sheen-bottom { stop-color: var(--sheen-dark); }
  .rule-edge { stop-color: var(--rule-glow); stop-opacity: 0.25; }
  .rule-core { stop-color: var(--rule-glow); stop-opacity: 1; }
  .designer-name {
    font-family: "Michroma", "Arial", sans-serif;
    font-size: 128px;
    fill: var(--name-silver);
  }
  .designer-title {
    font-family: "Arimo", "Arial", sans-serif;
    font-weight: 700;
    font-size: 35px;
    fill: var(--tagline-white);
  }
</style>
</head>
<body>
  <svg class="business-card" viewBox="0 0 1200 600" xmlns="http://www.w3.org/2000/svg" role="img" aria-label="Rowan Tate, Professional Hair Designer">
    <defs>
      <clipPath id="card-shape">
        <rect x="0" y="0" width="1200" height="600" rx="28" ry="28"/>
      </clipPath>
      <linearGradient id="sheen" x1="0" y1="0" x2="0.35" y2="1">
        <stop offset="0" class="sheen-top"/>
        <stop offset="1" class="sheen-bottom"/>
      </linearGradient>
      <linearGradient id="rule-glow" x1="0" y1="0" x2="1" y2="0">
        <stop offset="0" class="rule-edge"/>
        <stop offset="0.55" class="rule-core"/>
        <stop offset="1" class="rule-edge"/>
      </linearGradient>
    </defs>

    <g clip-path="url(#card-shape)">
      <rect class="card-face" x="0" y="0" width="1200" height="600"/>
      <polygon class="card-sheen" points="885,0 1200,0 1200,600 655,600" fill="url(#sheen)"/>
    </g>

    <text class="designer-name" x="118" y="205" textLength="987" lengthAdjust="spacingAndGlyphs">ROWAN TATE</text>
    <rect class="name-rule" x="118" y="207" width="987" height="3" fill="url(#rule-glow)"/>
    <text class="designer-title" x="122" y="282" textLength="978" lengthAdjust="spacing">PROFESSIONAL HAIR DESIGNER</text>
  </svg>
</body>
</html>
```